Corporate Brochure for boutique Australian financial planning firm

We are looking for a face-lift with our company corporate brochure. This brochure will be used to show who we are, what we do, etc. to new potential clients. It will form part of an introductory pack that we give to clients after an initial free consultation.

The target market is generally people over 45 years old, including couples and singles, seeking financial advice.

We have a new logo and would like to implement elements of the logo design into the brochure.

There is a bit of text on the brochure so perhaps 3 double sided A4 pages (6 pages in total) with a trifold might work best.

The colours in our logo are black and red. We are looking to use these colours and maybe also white and grey?

We are after a contemporary, clean, minimalist design using elements/shapes/forms of our logo design in there so it's not generic and speaks out as 'ours'. It needs to be professional but not traditional looking if that makes sense.

This brochure will be used in emails but mostly in print form so it needs to be designed print-ready but in a readable format that we can also send via email.

Here are some things that might help, including attachments:
Our company website: http://merrowplanning.com.au

NOTE
In the New Corporate Brochure Content attachment, the pages have been laid out with printing in mind. So pages 1-3 in the PDF are for the "inside" of the brochure, pages 4-6 are for the "outside" of the brochure. So the front page would be page 6 from the PDF, and the back page would be page 4.

Target Market(s)

Australian couples and singles generally over 45 years old who are seeking financial advice

Industry/Entity Type

Financial Planning

Font styles to use
Sans Serif

Requirements
Must have
• Print-ready for 3 double sided A4 pages (6 pages in total with a trifold)
• Our company logo + other graphics (all in 'Must Use' graphics folder)
• The red colour that's in our logo.
• White background - clean aesthetic.
• Our financial planning process graphic can be kept as is or re-designed to suit space.
Should not have
• Title 'Corporate Brochure'

```html
<!DOCTYPE html>
<html lang="en">
<head>
<meta charset="utf-8">
<title>Merrow Planning – Brochure Inside Spread</title>
<link href="https://fonts.googleapis.com/css2?family=Open+Sans:ital,wght@0,400;0,600;0,700;1,400;1,700&display=swap" rel="stylesheet">
<style>
  :root{
    --red:#e2332b;
    --ink:#2b2b2b;
    --charcoal:#2e2d2f;
    --grey:#8a8a8a;
    --rule:#9a9a9a;
    --paper:#ffffff;
    --backdrop:#e6e6e6;
  }
  *{box-sizing:border-box;margin:0;padding:0}
  html,body{width:1200px;height:785px;overflow:hidden}
  body{background:var(--backdrop);font-family:"Open Sans",Arial,sans-serif;color:var(--ink)}
  .spread{position:absolute;left:45px;top:118px;width:1110px;height:550px;display:flex;box-shadow:0 10px 30px rgba(0,0,0,.18)}
  .panel{width:370px;height:100%;position:relative;overflow:hidden}
  .panel + .panel{border-left:1px solid #e2e2e2}
  .section-title{display:flex;align-items:center;gap:10px;font-weight:700;font-size:17px;line-height:1.1}
  .section-title::before{content:"";width:11px;height:11px;background:var(--red);flex:none}

  /* Adviser panel */
  .panel--adviser{background:var(--charcoal);color:#fff}
  .adviser-photo{position:absolute;left:0;top:40px;width:140px;height:510px;background:linear-gradient(180deg,#8a8f98 0%,#3c4454 35%,#262c3a 100%)}
  .adviser-copy{position:absolute;left:150px;top:32px;width:208px;font-size:9.2px;line-height:1.38}
  .adviser-copy .section-title{color:#fff;margin-bottom:10px;font-size:15px}
  .adviser-copy .role{font-weight:700;margin-bottom:2px}
  .adviser-copy .name{color:var(--red)}
  .adviser-copy ul{list-style:none;margin:2px 0 7px}
  .adviser-copy li{font-style:italic}
  .adviser-copy li::before{content:"";display:inline-block;width:5px;height:5px;background:var(--red);margin:0 6px 1px 0}
  .adviser-copy p{margin-bottom:7px}
  .badges{position:absolute;left:172px;bottom:18px;display:flex;gap:44px}
  .badge{width:54px;height:54px;border-radius:50%}
  .badge--award{background:#2f6fc4;border:3px solid #9fc1ea}
  .badge--trust{background:#4a5258;border:2px solid #7b868c}

  /* Process panel */
  .panel--process{background:var(--paper);padding:28px 22px 0 20px}
  .process-intro{font-size:9px;font-weight:700;font-style:italic;line-height:1.38;margin:10px 0 14px}
  .steps{list-style:none;position:relative}
  .steps::before{content:"";position:absolute;left:87px;top:4px;bottom:6px;width:1.5px;background:var(--rule)}
  .step{display:grid;grid-template-columns:78px 1fr;gap:20px;margin-bottom:11px;position:relative}
  .step:last-child{margin-bottom:0}
  .step::after{content:"";position:absolute;left:84px;top:2px;width:8px;height:8px;border-radius:50%;background:var(--rule)}
  .step-label{text-align:right;font-size:9px;color:var(--grey);line-height:1.3;padding-top:30px}
  .step-label strong{display:block;color:var(--red);font-weight:700;font-size:9.5px}
  .step-body h3{font-size:9.2px;font-weight:700;font-style:italic;line-height:1.35;margin-bottom:2px}
  .step-body p{font-size:8.8px;line-height:1.38}

  /* Questions panel */
  .panel--questions{background:var(--paper);padding:28px 26px 0 24px}
  .panel--questions .section-title{margin-bottom:16px}
  .questions{list-style:none}
  .question{display:grid;grid-template-columns:26px 1fr;margin-bottom:10px}
  .question-num{color:var(--red);font-weight:700;font-size:12px}
  .question h3{font-size:9.5px;font-weight:700;font-style:italic;margin-bottom:2px}
  .question p{font-size:9px;line-height:1.42}
  .press{display:grid;grid-template-columns:repeat(4,1fr);gap:14px 10px;margin-top:18px;align-items:center}
  .press-name{font-size:8.5px;font-weight:700;color:var(--ink);display:flex;align-items:center;gap:4px;line-height:1.15}
  .press-name i{width:7px;height:7px;background:var(--red);flex:none}
</style>
</head>
<body>
<main class="spread">

  <section class="panel panel--adviser">
    <div class="adviser-photo" role="img" aria-label="Portrait photograph of the adviser in a navy suit, smiling"></div>
    <div class="adviser-copy">
      <h2 class="section-title">Meet Your Adviser</h2>
      <p class="role">Director &amp; Principal Financial Adviser <span class="name">CALLUM REEVES</span></p>
      <ul>
        <li>Winner of the 2016 GWA Adviser of the Year</li>
        <li>2016 Most Trusted Adviser</li>
      </ul>
      <p>Callum Reeves is the Director of Merrow Planning. He was awarded the prestigious ‘Adviser of the Year’ accolade in 2016 by the Guild of Wealth Advisers and was selected to join the Trusted Adviser Circle as a result of outstanding feedback from his clients. Callum has a Bachelor of Mathematics. He is an accredited SMSF Specialist Advisor, a certified financial planner and one of Australia’s only financial life planners.</p>
      <p>A born and bred Northern Beaches boy, he has an active interest in many sports and with two young boys, you won’t see him sitting idle. Between refereeing local football matches, teaching his boys to surf or lining up a birdie putt on the golf course, when he isn’t working, Callum is ‘on the go’.</p>
      <p>You may have seen him occasionally on Vista TV’s Horizon News business program Money Matters Live, or quoted in publications including the Harbour Ledger or the Coastline Herald.</p>
    </div>
    <div class="badges">
      <div class="badge badge--award" role="img" aria-label="Adviser of the Year award badge"></div>
      <div class="badge badge--trust" role="img" aria-label="Trusted adviser certificate badge"></div>
    </div>
  </section>

  <section class="panel panel--process">
    <h2 class="section-title">Our Financial Planning Process</h2>
    <p class="process-intro">Merrow Planning reach your goals. This prides itself on lifelong plan will form the relationship foundation of how we and we encourage you to work together; take the time necessary to be comfortable with all aspects of our proposal prior to taking the next step.</p>
    <ol class="steps">
      <li class="step">
        <div class="step-label">Step One<strong>DISCOVERY</strong></div>
        <div class="step-body">
          <h3>No two human beings are exactly alike and similarly, no two financial plans are the same</h3>
          <p>This is the time where we listen and learn about you, your values, your aspirations, your financial goals. We work with you to determine how we can help you reach your goals. We look at where you are, where you want to go and find a way to get there.</p>
        </div>
      </li>
      <li class="step">
        <div class="step-label">Step Two<strong>INTERPRET</strong></div>
        <div class="step-body">
          <h3>Did we hear you correctly?</h3>
          <p>We want to make sure we understand you. So we send you an interpretation paper with a complete diagnosis of your current financial situation and our recommendations on the strategy required to reach your goals. This plan will form the foundation of how we work.</p>
        </div>
      </li>
      <li class="step">
        <div class="step-label">Step Three<strong>MUTUAL<br>COMMITMENT</strong></div>
        <div class="step-body">
          <h3>Let’s implement!</h3>
          <p>We work with you to implement your plan over the areas relevant to your individual goal. We meet with you to outline the results you can expect in the short and long term path to your financial security, and we keep you abreast of the picture. This is the exciting part.</p>
        </div>
      </li>
      <li class="step">
        <div class="step-label">Step Four<strong>90 DAY<br>FOLLOW-UP</strong></div>
        <div class="step-body">
          <h3>Check that everything is in place.</h3>
          <p>We meet to recap the results you can expect and to answer your questions. We also understand that things can change. That’s why we review and adjust your financial plan as necessary. We are on your side.</p>
        </div>
      </li>
    </ol>
  </section>

  <section class="panel panel--questions">
    <h2 class="section-title">5 Questions for Callum</h2>
    <ol class="questions">
      <li class="question"><span class="question-num">1.</span><div>
        <h3>What do you love most about your career?</h3>
        <p>Being able to help people live their ideal life and helping them understand how to use money.</p></div></li>
      <li class="question"><span class="question-num">2.</span><div>
        <h3>What is your experience as a financial adviser?</h3>
        <p>I’ve always worked in a small, self-licensed business so my experience is more around solving clients’ most pressing financial challenges rather than meeting a sales target. Boutique firms tend to work differently to banks and large institutions.</p></div></li>
      <li class="question"><span class="question-num">3.</span><div>
        <h3>What type of clients do you specialise in?</h3>
        <p>We look after 3 types of clients. Firstly, people who are suddenly single and face making financial decisions alone, often for the first time. Secondly, those who are winding down and want to spend their remaining working years trying to teach themselves finance. And thirdly, couples with good incomes but no time to dedicate to their own financial wellbeing.</p></div></li>
      <li class="question"><span class="question-num">4.</span><div>
        <h3>What are the things you value most in life?</h3>
        <p>9 hours of sleep each night and weekends with family.</p></div></li>
      <li class="question"><span class="question-num">5.</span><div>
        <h3>If you won the lottery tomorrow, how would you live your life?</h3>
        <p>I would continue to align my values with my actions. And buy a better second-hand surfboard.</p></div></li>
    </ol>
    <div class="press" aria-label="As featured in">
      <span class="press-name">Harbour Ledger</span>
      <span class="press-name">Coastline Herald</span>
      <span class="press-name">Investor Weekly</span>
      <span class="press-name">Daily Dispatch</span>
      <span class="press-name"><i></i>GWA</span>
      <span class="press-name">Vista TV</span>
      <span class="press-name">National Courier</span>
      <span class="press-name">Adviser Monthly</span>
      <span class="press-name">Bayside Times</span>
      <span class="press-name">Metro Nine</span>
      <span class="press-name">Channel North</span>
      <span class="press-name"><i></i>Horizon News</span>
    </div>
  </section>

</main>
</body>
</html>
```